Business Card Design Project

This design is a slimline business card 45mm x90mm, the card will be printed at 49mm x 94mm and cut to 45mm x90 mm, this needs to be considered in the design. The content required on the front and back of the business card is attached in a pdf; the design will be done using photo shop as we use CS6 in our business. The design needs to be developed using a CMYK colour pallet, the main colours used on our business are red, grey black and white. A snapshot of our business brochure and new website has been provided to give you an understanding on our businesses look and feel.
FRONT OF BUSINESS CARD
Director
Marcus Feld
Ph+61 0421780213
www.brightvanecontracting.com.au
marcusfeld@brightvanecontracting.com.au
BACK OF BUSINESS CARD
SUPPORTING CLIENTS IN
Oil & Gas I Minerals & Metals I Petrochemical I Manufacturing
Building & Construction I Telecommunication I Rail I Civil I New Industries
KNOWLEDGE I EXPERTISE I EXPERIENCE I CAPACITY

```html
<!DOCTYPE html>
<html lang="en">
<head>
<meta charset="utf-8">
<title>Business Card – Back</title>
<link rel="stylesheet" href="https://fonts.googleapis.com/css2?family=Source+Sans+3:wght@400&display=swap">
<style>
  :root {
    --card-white: #ffffff;
    --brand-red: #ed1c24;
    --sector-grey: #9b9b9b;
    --value-ink: #231f20;
    --crop-ink: #231f20;
  }
  html, body {
    margin: 0;
    padding: 0;
    width: 1200px;
    height: 626px;
    overflow: hidden;
    background: var(--card-white);
  }
  .card-back {
    position: relative;
    width: 1200px;
    height: 626px;
    background: var(--card-white);
    font-family: "Source Sans 3", "Myriad Pro", Arial, sans-serif;
    font-weight: 400;
  }
  .crop-marks {
    position: absolute;
    inset: 0;
  }
  .headline {
    position: absolute;
    top: 148px;
    left: 0;
    width: 100%;
    margin: 0;
    text-align: center;
    color: var(--brand-red);
    font-size: 55px;
    font-weight: 400;
    line-height: 64px;
    letter-spacing: -0.5px;
  }
  .sector-list {
    position: absolute;
    top: 218px;
    left: 0;
    width: 100%;
    margin: 0;
    padding: 0;
    list-style: none;
    text-align: center;
    color: var(--sector-grey);
    font-size: 33px;
    line-height: 44px;
  }
  .sector-list li { margin: 0; }
  .values {
    position: absolute;
    top: 435px;
    left: 0;
    width: 100%;
    margin: 0;
    text-align: center;
    color: var(--value-ink);
    font-size: 30px;
    line-height: 38px;
  }
  .sep { padding: 0 0.32em; }
  .brand-band {
    position: absolute;
    left: 0;
    top: 590px;
    width: 100%;
    height: 9px;
    background: var(--brand-red);
  }
</style>
</head>
<body>
  <main class="card-back">
    <svg class="crop-marks" width="1200" height="626" viewBox="0 0 1200 626" aria-hidden="true">
      <g stroke="var(--crop-ink)" stroke-width="1" fill="none">
        <path d="M24.5 0 V24.5 H0"/>
        <path d="M1175.5 0 V24.5 H1200"/>
        <path d="M24.5 626 V602.5 H0"/>
        <path d="M1175.5 626 V602.5 H1200"/>
      </g>
    </svg>

    <h1 class="headline">SUPPORTING CLIENTS IN</h1>

    <ul class="sector-list">
      <li>Oil &amp; Gas<span class="sep">|</span>Minerals &amp; Metals<span class="sep">|</span>Petrochemical<span class="sep">|</span>Manufacturing</li>
      <li>Building &amp; Construction<span class="sep">|</span>Telecommunication<span class="sep">|</span>Rail</li>
      <li>Civil<span class="sep">|</span>New Industries</li>
    </ul>

    <p class="values">KNOWLEDGE<span class="sep">|</span>EXPERTISE<span class="sep">|</span>EXPERIENCE<span class="sep">|</span>CAPACITY</p>

    <div class="brand-band"></div>
  </main>
</body>
</html>
```